Plumbing Company After Business Card

Business card for a plumbing business that offers a variety of plumbing services including maintenance, domestic and commercial plumbing. My main focus is to offer high quality professional service. A logo on the card would be ideal. Any other questions feel free to email. Cheers

Looking for something modern and upmarket with preferably a matte black background

Business name is Keystone Plumbing and Gas

Industry/Entity Type

Plumbing

Contact Information for Business Card

Keystone Plumbing and Gas
Marcus Thornell
0427915368
14 Corrigan Road, Elmvale 3561
keystoneplumbing@mailbay.com.au
ABN 52 647 183 925

Font styles to use
Sans Serif

Colors
1b1b1b
ffffff
3377b5

Requirements
Must have
• Domestic
• Commercial
• Maintenance

```html
<!DOCTYPE html>
<html lang="en">
<head>
<meta charset="utf-8">
<title>Keystone Plumbing and Gas – Business Card</title>
<link rel="stylesheet" href="https://fonts.googleapis.com/css2?family=Open+Sans:wght@400;600;700;800&display=swap">
<style>
  :root {
    --matte-black: #1b1b1b;
    --card-black: #161616;
    --white: #ffffff;
    --brand-blue: #3377b5;
    --deep-blue: #1f4fa8;
    --bright-blue: #2a63d4;
    --flame-orange: #e2701c;
    --flame-red: #d7361f;
    --text-grey: #e4e4e4;
    --stage: #e9e7e3;
  }
  * { margin: 0; padding: 0; box-sizing: border-box; }
  html, body {
    width: 1200px; height: 843px; overflow: hidden;
    background: var(--stage);
    font-family: "Open Sans", sans-serif;
  }
  .sheet {
    width: 1200px; height: 843px;
    display: flex; align-items: center; justify-content: center; gap: 40px;
  }
  .card {
    position: relative;
    width: 540px; height: 330px;
    border-radius: 16px;
    overflow: hidden;
    box-shadow: 0 10px 28px rgba(0,0,0,.22);
  }

  /* Back side */
  .card--back {
    background: radial-gradient(ellipse at 50% 40%, var(--bright-blue) 0%, var(--deep-blue) 70%, #173e8a 100%);
    color: var(--white);
    display: flex; flex-direction: column; align-items: center; justify-content: center;
    text-align: center;
  }
  .back-wordmark {
    font-size: 40px; font-weight: 800; line-height: 1.05; letter-spacing: .5px;
    text-transform: uppercase;
  }
  .back-services {
    margin-top: 26px; font-size: 15px; font-weight: 400; letter-spacing: .4px;
  }

  /* Front side */
  .card--front { background: var(--card-black); color: var(--text-grey); }
  .front-brand {
    position: absolute; left: 34px; top: 72px; width: 210px;
    display: flex; align-items: center; gap: 12px;
  }
  .brand-dot {
    flex: none; width: 40px; height: 40px; border-radius: 50%;
    background: var(--brand-blue);
  }
  .brand-name {
    font-size: 24px; font-weight: 800; line-height: 1.05;
    color: var(--brand-blue); text-transform: uppercase;
  }
  .front-divider {
    position: absolute; left: 262px; top: 52px; width: 1px; height: 120px;
    background: linear-gradient(to bottom, rgba(255,255,255,0), rgba(255,255,255,.6), rgba(255,255,255,0));
  }
  .contact {
    position: absolute; left: 284px; top: 58px;
    font-size: 13.5px; line-height: 1.55;
  }
  .contact-name {
    font-size: 18px; font-weight: 600; letter-spacing: 1px;
    color: var(--bright-blue); text-transform: uppercase; margin-bottom: 6px;
  }
  .contact-label { font-weight: 700; color: var(--white); }

  .service-band { position: absolute; left: 0; bottom: 0; width: 540px; height: 110px; }
  .service-list {
    position: absolute; left: 40px; bottom: 62px;
    font-size: 14px; color: #0e1d3a; letter-spacing: .3px;
  }
</style>
</head>
<body>
<main class="sheet">

  <section class="card card--back" aria-label="Card back">
    <div class="back-wordmark">Keystone<br>Plumbing &amp; Gas</div>
    <p class="back-services">Domestic | Commercial | Maintenance</p>
  </section>

  <section class="card card--front" aria-label="Card front">
    <div class="front-brand">
      <span class="brand-dot"></span>
      <span class="brand-name">Keystone Plumbing &amp; Gas</span>
    </div>

    <div class="front-divider"></div>

    <address class="contact" style="font-style:normal">
      <div class="contact-name">Marcus Thornell</div>
      <div>14 Corrigan Road, Elmvale 3561</div>
      <div><span class="contact-label">Phone :</span> 042 791 5368</div>
      <div>keystoneplumbing@mailbay.com.au</div>
      <div>ABN 52 647 183 925</div>
    </address>

    <svg class="service-band" viewBox="0 0 540 110" aria-hidden="true">
      <defs>
        <linearGradient id="bandBlue" x1="0" x2="1">
          <stop offset="0" stop-color="#2a5fc9"/>
          <stop offset="1" stop-color="#1e49a6"/>
        </linearGradient>
        <linearGradient id="bandOrange" x1="0" x2="1">
          <stop offset="0" stop-color="#d7361f"/>
          <stop offset="1" stop-color="#e98a1c"/>
        </linearGradient>
      </defs>
      <polygon points="0,26 395,70 395,92 0,48" fill="url(#bandBlue)"/>
      <polygon points="395,70 540,86 540,108 395,92" fill="url(#bandOrange)"/>
      <circle cx="392" cy="80" r="16" fill="var(--brand-blue)"/>
    </svg>
    <p class="service-list" style="transform:rotate(6.3deg);transform-origin:left center">Domestic | Commercial | Maintenance</p>
  </section>

</main>
</body>
</html>
```